依頼詳細
①洋服(女性・男性・子供・ナチュラル)・ブランド品・携帯電話買取の要素を1つにまとめて下さい。添付ファイルにて数種類のチラシを添付しました。今まではそれぞれ使っていたのですが、1枚にまとめいたいと思います。
②宅配買取ではなく、店頭持ち込みの買取を強化したいと思っております。
(地図データを作成し入れて下さい。)
③今までのデザインには全くこだわっておりません。むしろ変えていただきたいと思います。
記載項目
店名:買取ルミナ・フリーダイヤル:0120-716-483・住所:〒 989-2783宮城県岩沼市北原台5丁目8-14  TEL:0223-47-1859  FAX:0223-47-3764
<定休日>土・日・祝 <営業時間>9:00~17:00 (買取の際は、事前にご連絡ください。)
買取サイト http://www.kaitori-lumina-example.com
販売サイト http://www.shop-lumina-example.com
サイズ
B4
ページ数
片面
希望イメージ
シンプル 複雑
単色 カラフル
暗い 明るい
日常 高級
遊び心 厳粛
未来的 伝統的
女性的 男性的
希望する色
緑系、黄・オレンジ系、緑系もしくは、オレンジ系で作成をお願いします。
納品ファイル
• イラストレーター形式 (.ai)
補足説明
参考までに今まで作製したチラシや素材を添付します。
あくまでも参考にしてください。真似る必要はありませんのでお願いします。

```html
<!DOCTYPE html>
<html lang="ja">
<head>
<meta charset="utf-8">
<title>買取ルミナ 店頭買取強化中</title>
<link href="https://fonts.googleapis.com/css2?family=Noto+Sans+JP:wght@400;700;900&display=swap" rel="stylesheet">
<style>
:root{
  --red:#e60012;
  --orange:#f39800;
  --orange-deep:#ec6c00;
  --yellow:#fff23f;
  --ink:#1a1a1a;
  --white:#ffffff;
  --photo-a:#d9dcdf;
  --photo-b:#a9adb2;
  --map:#f4f1e6;
}
*{margin:0;padding:0;box-sizing:border-box}
html,body{width:846px;height:1200px;overflow:hidden;background:var(--white)}
body{font-family:"Noto Sans JP",sans-serif;color:var(--ink)}
.flyer{position:relative;width:846px;height:1200px;overflow:hidden;background:var(--white)}
.abs{position:absolute}

.photo{left:0;top:150px;width:846px;height:540px;
  background:radial-gradient(ellipse at 70% 45%,var(--photo-a),var(--photo-b) 70%,#e8e9ea 100%);}
.photo-fade{left:0;top:150px;width:620px;height:250px;background:linear-gradient(180deg,#fff 0%,#fff 70%,rgba(255,255,255,0) 100%)}

.headline{left:36px;top:-8px;font-size:176px;font-weight:900;color:var(--red);letter-spacing:-6px;line-height:1.15;white-space:nowrap}
.shout{left:610px;top:40px;width:220px;font-size:34px;font-weight:900;line-height:1.25;transform:rotate(18deg);transform-origin:left top}
.lead{left:52px;top:196px;font-size:52px;font-weight:900;line-height:1.25;letter-spacing:1px;white-space:nowrap}
.lead-main{left:38px;top:258px;font-size:104px;font-weight:900;color:var(--red);line-height:1.1;letter-spacing:-2px;white-space:nowrap}
.whoop{left:40px;top:535px;font-size:34px;font-weight:900;transform:rotate(-62deg);transform-origin:left top;white-space:nowrap}

.tape{left:0;top:560px;width:846px;height:90px}

.badge{left:323px;top:420px;width:204px;height:204px;border-radius:50%;background:var(--orange);
  display:flex;flex-direction:column;align-items:center;justify-content:center;color:var(--white);
  font-weight:900;font-size:40px;line-height:1.2;border:5px solid var(--white);transform:rotate(-8deg)}

.cat{top:607px;height:226px;background:var(--white);border-radius:14px;overflow:hidden;text-align:center;box-shadow:0 0 0 3px var(--white)}
.cat-head{height:92px;color:var(--white);display:flex;flex-direction:column;align-items:center;justify-content:center}
.cat-title{font-size:40px;font-weight:900;line-height:1.1;white-space:nowrap}
.cat-sub{font-size:9px;font-weight:700;margin-top:6px;white-space:nowrap}
.cat-body{padding:14px 8px 0;font-size:15px;font-weight:700;line-height:1.5;white-space:nowrap}
.cat--mobile{left:212px;width:184px}
.cat--mobile .cat-head{background:var(--red)}
.cat--mobile .cat-body{color:var(--red)}
.cat--wear{left:423px;width:197px}
.cat--wear .cat-head,.cat--brand .cat-head{background:var(--orange)}
.cat--wear .cat-body,.cat--brand .cat-body{color:var(--orange-deep)}
.cat--brand{left:635px;width:197px}

.footer{left:0;top:840px;width:846px;height:360px;background:var(--yellow)}
.map{left:14px;top:850px;width:312px;height:322px;background:var(--map);border:3px solid var(--ink)}
.info{left:340px;top:846px;width:496px}
.ask{font-size:19px;font-weight:700;text-align:center;white-space:nowrap}
.freedial{margin-top:6px;height:70px;background:var(--white);border:3px solid var(--red);display:flex;align-items:center;justify-content:center;gap:12px;white-space:nowrap}
.fd-mark{background:var(--red);color:var(--white);font-size:14px;font-weight:900;padding:3px 8px;border-radius:4px}
.fd-num{font-size:46px;font-weight:900;line-height:1}
.shop{margin-top:8px;display:flex;align-items:center;gap:12px}
.shop-dot{width:22px;height:22px;background:var(--red)}
.shop-name{font-size:48px;font-weight:900;color:var(--red);line-height:1}
.shop-kind{font-size:17px;font-weight:700;line-height:1.3}
.addr{margin-top:8px;font-size:19px;font-weight:700;line-height:1.45;white-space:nowrap}
.hours{font-size:17px}
.mail{margin-top:4px;font-size:17px;font-weight:700;display:flex;gap:8px;align-items:center;white-space:nowrap}
.tag{background:var(--red);color:var(--white);padding:0 8px;font-size:14px;border-radius:3px}
.web{margin-top:4px;font-size:16px;font-weight:700;display:flex;gap:8px;align-items:center;white-space:nowrap}
</style>
</head>
<body>
<main class="flyer">
  <div class="abs photo" role="img" aria-label="ゴールテープを切って笑顔で走り込む男性と女性の写真"></div>
  <div class="abs photo-fade"></div>

  <h1 class="abs headline">急げ!!</h1>
  <p class="abs shout">ルミナが<br>買ってくれるぞー!</p>
  <p class="abs lead">店頭持ち込みによる</p>
  <h2 class="abs lead-main">買取強化中!</h2>
  <p class="abs whoop">ヒャッホー!</p>

  <svg class="abs tape" viewBox="0 0 846 90" aria-hidden="true">
    <path d="M0 40 Q420 70 846 20 L846 34 Q420 84 0 54 Z" fill="var(--red)"/>
  </svg>

  <div class="abs badge"><span>いろいろ</span><span>買います</span></div>

  <section class="abs cat cat--mobile">
    <div class="cat-head"><span class="cat-title">携帯</span><span class="cat-sub">ケータイ電話・スマートフォン全機種</span></div>
    <p class="cat-body">使わなくなった<br>ケータイは、<br>高く売って、買い<br>替えに役立てよう!</p>
  </section>
  <section class="abs cat cat--wear">
    <div class="cat-head"><span class="cat-title">洋服</span><span class="cat-sub">メンズ・レディース・キッズ服・バッグ・小物等</span></div>
    <p class="cat-body">オールシーズン<br>どの季節のお洋服でも<br>お買取いたします。<br>お気軽にどうぞ。</p>
  </section>
  <section class="abs cat cat--brand">
    <div class="cat-head"><span class="cat-title">ブランド</span><span class="cat-sub">バッグ・財布・時計・アクセサリー・コスメ</span></div>
    <p class="cat-body">人気ブランド各種の<br>バッグ・財布・小物等<br>お売り下さい!</p>
  </section>

  <div class="abs footer"></div>
  <div class="abs map" role="img" aria-label="店舗周辺の案内地図"></div>

  <section class="abs info">
    <p class="ask">「これいくら?」などお値段のお問合せもお気軽に</p>
    <div class="freedial"><span class="fd-mark">フリーダイヤル</span><span class="fd-num">0120-716-483</span></div>
    <div class="shop">
      <span class="shop-dot"></span>
      <span class="shop-name">ルミナ</span>
      <span class="shop-kind">Kids &amp; Ladys<br>リサイクルブランド館</span>
    </div>
    <p class="addr">〒 989-2783 宮城県岩沼市北原台5丁目8-14<br>TEL 0223-47-1859 FAX 0223-47-3764<br><span class="hours">営業時間 9:00〜17:00 定休日 土・日・祝</span></p>
    <p class="mail"><span class="tag">メール</span>info@shop-lumina-example.com</p>
    <p class="web"><span class="tag">買取</span>http://www.kaitori-lumina-example.com</p>
    <p class="web"><span class="tag">WEB</span>http://www.shop-lumina-example.com</p>
  </section>
</main>
</body>
</html>
```